Tobin's Jewelry Studio Needs a Moving Location Flyer

We need a flyer to inform our customers of our location moving. We will be moving to our city's downtown which is only 1 mile away from our current address. We will be having a moving sale ( Up to 80% off). The sale starts Sept. 8th Our business creates, sells, and repairs fine jewelry. Dimensions are 5"x8"

Target Market(s)

Women ages 25-55

Industry/Entity Type

Jewelry

Colors
85abd2
cfdeed

Requirements
Must have
• Our logo
• Mention of the sale
• Our current address
• 4785 Cresthaven Blvd.
• Dunmore, Ca 94318
• (415)826-3319
Nice to have
• Mention that we're relocating to downtown Dunmore (new location opening Nov. 1st.)

```html
<!DOCTYPE html>
<html lang="en">
<head>
<meta charset="utf-8">
<title>Tobin's Jewelry Studio – Relocation Sale</title>
<link rel="stylesheet" href="https://fonts.googleapis.com/css2?family=Great+Vibes&family=Open+Sans:ital,wght@0,400;0,600;0,700;1,400;1,600;1,700&display=swap">
<style>
  :root {
    --sky: #85abd2;
    --mist: #cfdeed;
    --ink: #1d1d1d;
    --brand-brown: #4a3a33;
    --accent-blue: #3a86c8;
    --sale-red: #e0261c;
    --paper: #ffffff;
  }
  * { margin: 0; padding: 0; box-sizing: border-box; }
  html, body { width: 849px; height: 1200px; overflow: hidden; background: #e9edf1; }
  .flyer {
    position: relative;
    width: 849px;
    height: 1200px;
    overflow: hidden;
    font-family: "Open Sans", Arial, sans-serif;
    color: var(--ink);
    background: linear-gradient(180deg, var(--paper) 0%, #f6f9fc 55%, var(--mist) 78%, var(--sky) 100%);
  }
  .brand-bar {
    position: absolute;
    top: 78px; left: 0; right: 0;
    display: flex; align-items: center; justify-content: center; gap: 22px;
  }
  .brand-bar .rule { width: 120px; height: 3px; background: var(--brand-brown); }
  .brand-mark { display: flex; align-items: center; gap: 16px; }
  .brand-dot { width: 58px; height: 58px; border-radius: 50%; background: var(--mist); }
  .brand-name { font-size: 30px; font-weight: 600; color: var(--brand-brown); letter-spacing: 0.5px; }
  .product-photo {
    position: absolute;
    left: 190px; top: 200px;
    width: 470px; height: 360px;
    border-radius: 40px;
    background: radial-gradient(ellipse at 50% 45%, #d9c9b8 0%, #a98b72 40%, #6a5244 70%, rgba(255,255,255,0) 100%);
  }
  .discount-badge {
    position: absolute;
    left: 650px; top: 530px;
    width: 150px; height: 150px;
    border-radius: 50%;
    background: var(--sale-red);
    border: 5px solid #fff;
    box-shadow: 0 3px 8px rgba(0,0,0,0.25);
    color: #fff;
    display: flex; flex-direction: column; align-items: center; justify-content: center;
    font-weight: 700; line-height: 1.05;
  }
  .discount-badge .lead { font-size: 22px; }
  .discount-badge .amount { font-size: 32px; }
  .headline {
    position: absolute;
    top: 640px; left: 0; right: 0;
    text-align: center;
    font-family: "Great Vibes", cursive;
    font-size: 76px; line-height: 74px;
    color: var(--ink);
  }
  .divider { position: absolute; top: 800px; left: 254px; width: 340px; height: 16px; }
  .sale-date {
    position: absolute; top: 820px; left: 0; right: 0;
    text-align: center; font-style: italic; font-size: 46px; color: var(--accent-blue);
  }
  .services {
    position: absolute; top: 888px; left: 0; right: 0;
    text-align: center; font-style: italic; font-size: 25px;
  }
  .call-line {
    position: absolute; top: 928px; left: 0; right: 0;
    text-align: center; font-style: italic; font-weight: 700; font-size: 44px;
  }
  .contact {
    position: absolute; top: 1000px; left: 0; right: 0;
    text-align: center; font-size: 19px; line-height: 28px;
  }
  .contact .web { font-weight: 700; }
</style>
</head>
<body>
<main class="flyer">
  <header class="brand-bar">
    <span class="rule"></span>
    <div class="brand-mark">
      <span class="brand-dot"></span>
      <span class="brand-name">Tobin's Jewelry Studio</span>
    </div>
    <span class="rule"></span>
  </header>

  <div class="product-photo" role="img" aria-label="Photo of four interlocking diamond rings in rose gold, white gold, yellow gold and black"></div>

  <div class="discount-badge">
    <span class="lead">UP TO</span>
    <span class="amount">80% off</span>
  </div>

  <h1 class="headline">We're relocating to<br>downtown Dunmore</h1>

  <svg class="divider" viewBox="0 0 340 16" aria-hidden="true">
    <line x1="0" y1="8" x2="155" y2="8" stroke="#1d1d1d" stroke-width="1.5"/>
    <polygon points="170,2 178,8 170,14 162,8" fill="#1d1d1d"/>
    <line x1="185" y1="8" x2="340" y2="8" stroke="#1d1d1d" stroke-width="1.5"/>
  </svg>

  <p class="sale-date">sale starts Sept. 8th</p>
  <p class="services">We creates, sells, and repairs fine jewelry</p>
  <p class="call-line">CALL US: (415)826-3319</p>

  <address class="contact">
    <span>4785 Cresthaven Blvd.- Dunmore, Ca 94318</span><br>
    <span>TobinsJewelryStudio@mailbox.com</span><br>
    <span class="web">www.tobinsjewelrystudio.com</span>
  </address>
</main>
</body>
</html>
```